Toy Company Needs a Web Site For a New Toy

We need a web site for a new toy called "Zippa Loop Trike". The bike is a plastic, non motorized ride on toy for kids ages 1.5 - 5 years of age. The bike is being launched in three colors, red, blue and pink, though we may include a black option too.

For the web site we want something bold and colorful that communicates fun, therefore NO dull colors like black or grey. Nothing too cluttered. We want the site to attract the attention of kids but also give the parents a sense of confidence in our professionalism as a trustworthy toy company. The home page should focus on the bike, with different views of the bike and a small write-up on some of its key features. We would also like the home page to have a video of the bike in play. A obvious link to the shopping basket must be present as well. The site must include a shopping basket and ordering system.

Attached is a screenshot of a site that has the colourfulness and playfulness that we are looking for. Please have a look.

The bike images attached are renderings from the CAD software, actual high res photos will be used when the site is developed.

The product logo is attached and MUST be used on the site. It must be BOLD and can be incorporated into the actual website design.

The site pages are:
Home
Gallery
Buy
Contact

Competitors:
www.brambleplay.example
www.quorvaride.example
I do not like either of their sites.

We only have one product at this time, so the site is to be focused on that product, not a whole catalog of products. It is really a single product with the ability to purchase.
Updates

Project Deadline Extended
Reason: I am extending this competition in order to give me more time to review each design and provide the feedback that the designers deserve.

Target Market(s)

Parents, children ages 1.5 - 5.

Industry/Entity Type

It Company

Colors
0555a3
eb1f27
9bcb3c
faed22
f78f20
f37022
e34197
a6459a
6b449b

Requirements
Must have
• Please use the logo attached, but feel free to use different colors.
Should not have
• Dull colors like black and grey

```html
<!DOCTYPE html>
<html lang="en">
<head>
<meta charset="utf-8">
<title>Zippa Loop Trike</title>
<link rel="stylesheet" href="https://fonts.googleapis.com/css2?family=Arvo:wght@700&family=Lato:wght@400&family=Roboto:ital,wght@0,400;0,500;1,400&display=swap">
<style>
:root{
  --red:#e2332c;
  --red-band:#e3342d;
  --blue:#2ea3d8;
  --sky:#4bbcec;
  --royal:#0555a3;
  --royal-deep:#044a8e;
  --green:#9bcb3c;
  --leaf:#556622;
  --pink:#e34197;
  --purple:#6b449b;
  --orange:#f78f20;
  --ink:#333;
  --text:#4f4f4f;
  --title:#555;
  --grey-line:#d4d4d4;
  --page:#f7f7f7;
}
*{box-sizing:border-box;margin:0;padding:0}
html,body{width:1108px;height:1200px;overflow:hidden}
body{position:relative;background:var(--page);font-family:"Roboto",Arial,sans-serif;color:var(--ink)}
.abs{position:absolute}

.top-rule{left:0;top:0;width:1108px;height:3px;background:var(--red)}
.header{left:0;top:3px;width:1108px;height:103px;background:linear-gradient(#fff,#f3f3f3)}
.utility{right:36px;top:19px;font-size:11.5px;letter-spacing:.5px;color:#555;display:flex;align-items:center;gap:9px}
.utility .sep{color:#999}
.nav{left:120px;top:73px;display:flex;gap:17px;font-size:13.5px;letter-spacing:.4px;color:#333}
.nav .on{color:var(--red)}
.nav .sep{color:#888}
.nav-pointer{left:130px;top:99px}
.search{left:785px;top:58px;width:203px;height:27px;border:1px solid #ddd;border-radius:2px;background:#f6f6f6;font-size:10.5px;font-style:italic;color:#999;padding:7px 10px}
.search svg{position:absolute;right:4px;top:4px}

.hero{left:0;top:106px;width:1108px;height:422px;background:linear-gradient(180deg,#2f86d6 0%,#58aee8 35%,#8fd0f3 55%,#7cc94a 72%,#46a42f 100%)}
.hero-grass{left:0;top:500px;width:1108px;height:28px;background:linear-gradient(#3aa53a,#1f812d)}
.hero-frame{left:120px;top:106px;width:868px;height:404px;background:#fff;box-shadow:0 3px 8px rgba(0,0,0,.3)}
.hero-photo{left:125px;top:108px;width:858px;height:397px;background:
  radial-gradient(ellipse 240px 150px at 300px 230px,rgba(235,31,39,.85) 0%,rgba(235,31,39,.55) 45%,rgba(235,31,39,0) 100%),
  linear-gradient(180deg,#79b43f 0%,#4f8f2c 40%,#3f7d2a 58%,#5a9a6a 78%,#4a8a5c 100%)}
.hero-leaf{left:640px;top:108px;width:343px;height:397px;background:var(--leaf)}
.hero-card{left:654px;top:139px;width:306px;height:313px;background:#fff;box-shadow:0 6px 10px rgba(0,0,0,.35);text-align:center}
.hero-card h1{font-family:"Arvo",Georgia,serif;font-weight:700;font-size:26px;line-height:32.3px;color:var(--red);padding-top:18px;white-space:nowrap}
.hero-card .arrows{margin-top:12px}
.hero-shade{left:0;top:528px;width:1108px;height:14px;background:linear-gradient(rgba(0,0,0,.08),rgba(0,0,0,0))}

.logo{left:497px;top:62px;width:110px;height:110px;border-radius:50%;background:#fff;box-shadow:0 2px 6px rgba(0,0,0,.25);display:flex;align-items:center;justify-content:center;text-align:center}
.logo span{font-family:"Arvo",Georgia,serif;font-weight:700;font-size:15px;line-height:17px;color:var(--red)}

.section-title{font-family:"Arvo",Georgia,serif;font-weight:700;color:var(--title)}
.section-title em{font-style:normal;color:var(--red)}
.welcome-title{left:120px;top:570px;font-size:20px}
.welcome-photo{left:120px;top:609px;width:204px;height:145px;background:
  radial-gradient(ellipse 85px 55px at 100px 88px,rgba(235,31,39,.85) 0%,rgba(235,31,39,0) 100%),
  linear-gradient(180deg,#79b43f 0%,#4a8c2c 50%,#5a9a6a 100%)}
.welcome-copy{left:342px;top:604px;font-family:"Lato",Arial,sans-serif;font-size:11.5px;line-height:21.2px;color:var(--text);white-space:nowrap}
.read-more{left:342px;top:741px;font-size:11.5px;letter-spacing:.4px;color:var(--blue)}
.divider{left:120px;top:778px;width:868px;height:1px;background:var(--grey-line)}

.gallery-title{left:120px;top:797px;font-size:18px}
.gallery-arrows{left:645px;top:800px}
.card{top:836px;width:172px}
.card .thumb{height:109px;border:3px solid #fff;box-shadow:0 0 0 1px #ddd}
.card .name{margin-top:12px;font-size:13.5px;color:var(--blue)}
.card .desc{margin-top:2px;font-size:11.5px;color:#333}
.card .details{margin-top:11px;font-size:11px;letter-spacing:.5px;color:var(--red)}
.red-bike{background:radial-gradient(ellipse 70px 35px at 86px 70px,rgba(235,31,39,.9),rgba(235,31,39,0)),linear-gradient(180deg,#7ab43f,#4a8c2c 60%,#5a9a6a)}
.blue-bike{background:radial-gradient(ellipse 70px 35px at 86px 70px,rgba(5,85,163,.95),rgba(5,85,163,0)),linear-gradient(180deg,#7ab43f,#4a8c2c 60%,#5a9a6a)}
.pink-bike{background:linear-gradient(135deg,#6fae3d 0%,#e34197 55%,#c02f7e 100%)}

.promo{left:702px;top:790px;width:295px;height:229px;background:var(--sky)}
.promo h2{position:absolute;left:11px;top:12px;font-family:"Arvo",Georgia,serif;font-weight:700;font-size:18px;color:#fff}
.promo h2 em{font-style:normal;color:#2b2b2b}
.promo .video{position:absolute;left:9px;top:46px;width:277px;height:173px;border:2px solid #fff;background:radial-gradient(ellipse 120px 60px at 130px 110px,rgba(5,85,163,.95),rgba(5,85,163,0)),linear-gradient(180deg,#7ab43f 0%,#4a8c2c 55%,#5a9a6a 100%);display:flex;align-items:center;justify-content:center}

.newsletter{left:0;top:1029px;width:1108px;height:74px;background:var(--red-band)}
.newsletter h3{position:absolute;left:119px;top:24px;font-family:"Arvo",Georgia,serif;font-weight:700;font-size:17.5px;color:#fff;letter-spacing:.2px}
.newsletter .field{position:absolute;left:470px;top:17px;width:380px;height:39px;background:#f7f7f7;border:1px solid #ccc;border-radius:2px;padding:12px 15px;font-size:13px;font-style:italic;color:#999}
.newsletter .button{position:absolute;left:859px;top:17px;width:129px;height:39px;background:var(--blue);color:#fff;font-family:"Arvo",Georgia,serif;font-weight:700;font-size:14.5px;letter-spacing:.5px;text-align:center;line-height:39px}

.footer{left:0;top:1103px;width:1108px;height:97px;background:linear-gradient(var(--royal),var(--royal-deep));border-top:2px solid #fff}
.footer-logo{left:121px;top:1118px;width:70px;height:70px;border-radius:50%;background:#fff;display:flex;align-items:center;justify-content:center;text-align:center;font-family:"Arvo",Georgia,serif;font-weight:700;font-size:10px;line-height:12px;color:var(--red)}
.legal{left:207px;top:1135px;font-size:11.5px;line-height:21px;color:#fff;letter-spacing:.3px}
.connect{left:812px;top:1141px;font-size:11px;letter-spacing:.4px;color:#fff}
.social{top:1139px;width:27px;height:27px;border-radius:3px}
</style>
</head>
<body>
<div class="abs top-rule"></div>
<header class="abs header"></header>

<div class="abs utility">
  <svg width="16" height="13" viewBox="0 0 16 13"><path d="M1 4h14l-2 8H3z" fill="#2ea3d8"/><path d="M5 4l3-3 3 3" fill="none" stroke="#2ea3d8" stroke-width="1.5"/></svg>
  <span>YOUR CART</span><span class="sep">|</span><span>SIGNUP NEWSLETTER</span>
</div>

<nav class="abs nav">
  <span class="on">HOME</span><span class="sep">|</span><span>GALLERY</span><span class="sep">|</span><span>BUY</span><span class="sep">|</span><span>CONTACT</span>
</nav>
<svg class="abs nav-pointer" width="20" height="8" viewBox="0 0 20 8"><path d="M0 8L10 0l10 8z" fill="#2ea3d8"/></svg>

<div class="abs search">Search Keyword...
  <svg width="20" height="18" viewBox="0 0 20 18"><circle cx="8" cy="7" r="5" fill="none" stroke="#e2332c" stroke-width="2"/><path d="M12 11l6 5" stroke="#e2332c" stroke-width="3" stroke-linecap="round"/></svg>
</div>

<section class="abs hero" role="img" aria-label="Playful illustrated backdrop of blue sky, rainbow, green hills and flowers"></section>
<div class="abs hero-grass"></div>
<div class="abs hero-frame"></div>
<div class="abs hero-photo" role="img" aria-label="Red plastic ride-on bike toy on a tree-lined park path"></div>
<div class="abs hero-leaf"></div>
<div class="abs hero-card">
  <h1>We Sell Plastic<br>Bike, Non<br>Motorized Ride<br>on Toy for<br>Kids Ages<br>1.5 - 5 Years<br>of Age.</h1>
  <svg class="arrows" width="66" height="34" viewBox="0 0 66 34"><path d="M16 3L4 17l12 14M50 3l12 14-12 14" fill="none" stroke="#777" stroke-width="5" stroke-linecap="round" stroke-linejoin="round"/></svg>
</div>
<div class="abs hero-shade"></div>

<div class="abs logo"><span>Zippa Loop<br>Trike</span></div>

<h2 class="abs section-title welcome-title">Welcome to <em>Zippa Loop Trike</em></h2>
<div class="abs welcome-photo" role="img" aria-label="Red ride-on bike toy on a park path"></div>
<p class="abs welcome-copy">Aliquam molestie, mi et imperdiet euismod, dui purus auctor tellus, et interdum lacus lectus et ante. Sed accumsan<br>sollicitudin sapien, sit amet adipiscing turpis gravida ac. In congue, neque ac lobortis volutpat, libero mauris varius mi,<br>vitae suscipit ipsum ligula vitae risus. Duis aliquam nibh a dui iaculis viverra id a velit. Vivamus egestas risus in magna<br>varius commodo. Sed semper viverra egestas. Etiam pretium porttitor lectus, vel ornare neque porta volutpat.<br>Aenean a nibh eget turpis vehicula tempus ac sed massa. Vestibulum dolor nulla, ultrices ac tincidunt sed, ultricies non est.<br>Suspendisse lobortis turpis in odio blandit ac interdum lorem euismod.</p>
<span class="abs read-more">READ MORE</span>
<div class="abs divider"></div>

<h2 class="abs section-title gallery-title">Our <em>Gallery</em></h2>
<svg class="abs gallery-arrows" width="36" height="16" viewBox="0 0 36 16"><path d="M8 2L3 8l5 6M28 2l5 6-5 6" fill="none" stroke="#555" stroke-width="2" stroke-linecap="round" stroke-linejoin="round"/></svg>

<article class="abs card" style="left:121px">
  <div class="thumb red-bike" role="img" aria-label="Red ride-on bike on a park path"></div>
  <div class="name">Product Name</div>
  <div class="desc">Duis aliquam nibh a dui iaculis.</div>
  <div class="details">DETAILS</div>
</article>
<article class="abs card" style="left:315px">
  <div class="thumb blue-bike" role="img" aria-label="Blue ride-on bike on grass"></div>
  <div class="name">Product Name</div>
  <div class="desc">Duis aliquam nibh a dui iaculis.</div>
  <div class="details">DETAILS</div>
</article>
<article class="abs card" style="left:508px">
  <div class="thumb pink-bike" role="img" aria-label="Close-up of a pink bike body and wheel"></div>
  <div class="name">Product Name</div>
  <div class="desc">Duis aliquam nibh a dui iaculis.</div>
  <div class="details">DETAILS</div>
</article>

<aside class="abs promo">
  <h2>Promotional <em>Video</em></h2>
  <div class="video" role="img" aria-label="Video still of the blue ride-on bike in a park">
    <svg width="44" height="44" viewBox="0 0 44 44"><circle cx="22" cy="22" r="21" fill="#fff" opacity=".9"/><path d="M17 12l14 10-14 10z" fill="#333"/></svg>
  </div>
</aside>

<section class="abs newsletter">
  <h3>Sign up for our Email Newsletter!</h3>
  <div class="field">Enter Email Address</div>
  <div class="button">SIGN UP NOW</div>
</section>

<footer class="abs footer"></footer>
<div class="abs footer-logo">Zippa Loop<br>Trike</div>
<div class="abs legal">Copyright ©2013.<br>All Right Reserved &nbsp;|&nbsp; Privacy Policy</div>
<span class="abs connect">CONNECT US</span>
<span class="abs social" style="left:888px;background:var(--orange)" aria-label="Social link"></span>
<span class="abs social" style="left:925px;background:var(--green)" aria-label="Social link"></span>
<span class="abs social" style="left:961px;background:var(--pink)" aria-label="Social link"></span>
</body>
</html>
```